Bref créative
TRVB Business cards and stationary
TRVB business cards
Use same font as used in my logo
Marcus Delaney
President
487 W. Harborview Lane
Suite 318
Coral Springs, FL 33065
marcus@trvb-example.com
www.trvb-example.com

```html
<!DOCTYPE html>
<html lang="en">
<head>
<meta charset="utf-8">
<title>TRVB Stationery Set</title>
<link href="https://fonts.googleapis.com/css2?family=Cinzel:wght@600&family=Open+Sans:wght@400;600&display=swap" rel="stylesheet">
<style>
  :root{
    --bg:#e4e4e4;
    --paper:#ffffff;
    --red:#b3121f;
    --red-dark:#7d0a14;
    --ink:#555555;
    --muted:#9a9a9a;
  }
  *{margin:0;padding:0;box-sizing:border-box}
  html,body{width:1200px;height:247px;overflow:hidden;background:var(--bg)}
  body{position:relative;font-family:"Open Sans",Arial,sans-serif;color:var(--ink)}
  .piece{position:absolute;background:var(--paper);box-shadow:0 1px 3px rgba(0,0,0,.25);overflow:hidden}
  .brand{font-family:"Cinzel",Georgia,serif;font-weight:600;color:var(--red);letter-spacing:.5px;display:flex;align-items:center;gap:3px;white-space:nowrap}
  .brand .dot{width:5px;height:5px;border-radius:50%;background:var(--red);flex:none}
  .brand.on-red{color:#fff}
  .brand.on-red .dot{background:#fff}
  .tiny{font-size:3px;line-height:4.2px;white-space:nowrap}

  /* business cards */
  .card{left:8px;width:100px;height:56px;padding:6px}
  .card.front{top:58px;display:flex;flex-direction:column;justify-content:center;gap:2px}
  .card.front .brand{font-size:11px}
  .card.front .band{position:absolute;left:0;top:0;width:100%;height:5px;background:var(--red)}
  .card.back{top:122px}
  .card.back .name{font-size:5px;font-weight:600;color:var(--red)}
  .card.back .role{font-size:3.6px;color:var(--muted);margin-bottom:3px}
  .card.back .bar{position:absolute;left:0;bottom:0;width:100%;height:3px;background:var(--red)}
  .card.alt{top:186px;height:52px;display:flex;align-items:center;justify-content:center}
  .card.alt .brand{font-size:9px}

  /* letterheads */
  .letter{top:12px;width:100px;height:226px;padding:9px 8px}
  .letter.one{left:118px}
  .letter.two{left:226px}
  .letter .brand{font-size:7px;margin-bottom:14px}
  .letter .body{font-size:3.4px;line-height:5px}
  .letter .sign{margin-top:10px;font-size:3.4px;line-height:5px;color:var(--red)}
  .letter .foot{position:absolute;left:8px;right:8px;bottom:8px;border-top:1px solid var(--red);padding-top:2px;font-size:2.6px;line-height:3.6px;color:var(--muted);text-align:center}

  /* notes */
  .note{left:336px;width:70px;height:34px;padding:4px}
  .note .brand{font-size:6px;margin-bottom:2px}
  .note.red{top:40px;background:var(--red)}
  .note.white{top:82px}
  .note.white2{top:122px}

  /* envelopes */
  .envelope{left:415px;width:88px;height:40px;padding:4px}
  .envelope.front{top:70px}
  .envelope.back{top:120px}
  .envelope .brand{font-size:5px;margin-bottom:1px}
  .envelope .to{position:absolute;left:38px;top:18px;font-size:3px;line-height:4px;color:var(--muted)}
  .envelope .stripe{position:absolute;left:0;bottom:0;width:100%;height:3px;background:var(--red)}
  .envelope.back svg{position:absolute;inset:0}

  /* folder */
  .folder{top:14px;height:222px}
  .folder.cover{left:515px;width:335px;background:linear-gradient(135deg,var(--red),var(--red-dark));display:flex;flex-direction:column;align-items:center;justify-content:center;gap:6px}
  .folder.cover .brand{font-size:22px;gap:5px}
  .folder.cover .brand .dot{width:9px;height:9px}
  .folder.cover .web{font-size:5px;color:#f3d6d8;letter-spacing:1px}
  .folder.inside{left:852px;width:338px;background:#f6f6f6}
  .folder.inside .pocket{position:absolute;left:0;bottom:0;width:100%;height:88px;background:var(--red)}
  .folder.inside .slot{position:absolute;left:130px;top:140px;width:78px;height:42px;background:var(--paper);padding:4px;box-shadow:0 1px 2px rgba(0,0,0,.3)}
  .folder.inside .slot .name{font-size:4.4px;font-weight:600;color:var(--red);margin-bottom:1px}
  .folder.inside .pocket .brand{position:absolute;right:12px;bottom:10px;font-size:8px}
</style>
</head>
<body>

  <div class="piece card front">
    <div class="band"></div>
    <div class="brand"><span class="dot"></span>TRVB</div>
    <div class="tiny" style="color:var(--muted)">www.trvb-example.com</div>
  </div>

  <div class="piece card back">
    <div class="name">Marcus Delaney</div>
    <div class="role">President</div>
    <div class="tiny">487 W. Harborview Lane<br>Suite 318<br>Coral Springs, FL 33065<br>(954) 555-0142<br>marcus@trvb-example.com</div>
    <div class="bar"></div>
  </div>

  <div class="piece card alt">
    <div class="brand"><span class="dot"></span>TRVB</div>
  </div>

  <div class="piece letter one">
    <div class="brand"><span class="dot"></span>TRVB</div>
    <div class="body">Dear Client,<br>Thank you for your interest in our services.</div>
    <div class="sign">Marcus Delaney<br>President</div>
    <div class="foot">487 W. Harborview Lane · Suite 318<br>Coral Springs, FL 33065 · www.trvb-example.com</div>
  </div>

  <div class="piece letter two">
    <div class="brand"><span class="dot"></span>TRVB</div>
    <div class="body">Dear Client,<br>Thank you for your interest in our services.</div>
    <div class="foot">487 W. Harborview Lane · Suite 318<br>Coral Springs, FL 33065 · www.trvb-example.com</div>
  </div>

  <div class="piece note red"><div class="brand on-red"><span class="dot"></span>TRVB</div></div>
  <div class="piece note white"><div class="brand"><span class="dot"></span>TRVB</div><div class="tiny">(954) 555-0142</div></div>
  <div class="piece note white2"><div class="brand"><span class="dot"></span>TRVB</div><div class="tiny">With compliments</div></div>

  <div class="piece envelope front">
    <div class="brand"><span class="dot"></span>TRVB</div>
    <div class="tiny" style="color:var(--muted)">487 W. Harborview Lane<br>Coral Springs, FL 33065</div>
    <div class="to">Recipient name<br>Street address</div>
    <div class="stripe"></div>
  </div>
  <div class="piece envelope back">
    <svg width="88" height="40" viewBox="0 0 88 40"><path d="M0 0 L44 22 L88 0" fill="none" stroke="#cfcfcf" stroke-width="1"/><rect x="0" y="37" width="88" height="3" fill="#b3121f"/></svg>
  </div>

  <div class="piece folder cover">
    <div class="brand on-red"><span class="dot"></span>TRVB</div>
    <div class="web">www.trvb-example.com</div>
  </div>
  <div class="piece folder inside">
    <div class="pocket"><div class="brand on-red"><span class="dot"></span>TRVB</div></div>
    <div class="slot">
      <div class="name">Marcus Delaney</div>
      <div class="tiny">President<br>marcus@trvb-example.com<br>www.trvb-example.com</div>
    </div>
  </div>

</body>
</html>
```